psd/html for a e wallet payment website designed

hi
i am in need of a psd / html for a whole website designed
the site is a e wallet /payment system i can i will provide a link to what type of style i am looking for but i can not stress this enough i do not want anyone replicating the website i am just providing the links to show you what kind of function and the content that is involved also, i have a srs with detailed pages you can read and refer to if need be
thanks of viewing
Vantoleaf.com
Brisklune.com
marblequivercoin.com
Qrdelivane.com

```html
<!DOCTYPE html>
<html lang="en">
<head>
<meta charset="utf-8">
<title>Paywisp – Wallet for Everywhere</title>
<link href="https://fonts.googleapis.com/css2?family=Open+Sans:wght@300;400;600;700;800&display=swap" rel="stylesheet">
<style>
:root{
  --blue:#3fa0cf;
  --blue-dark:#2f8fc0;
  --orange:#d9400b;
  --ink:#111;
  --grey:#555;
  --grey-light:#e9e9e9;
  --white:#fff;
  --muted:#8a8a8a;
}
*{box-sizing:border-box;margin:0;padding:0}
html,body{width:1026px;height:1200px;overflow:hidden}
body{font-family:"Open Sans",Arial,sans-serif;background:var(--white);position:relative;color:var(--ink)}

/* header */
.site-header{position:absolute;left:0;top:0;width:1026px;height:67px;background:var(--white);border-bottom:1px dashed #bbb}
.brand{position:absolute;left:137px;top:20px;display:flex;align-items:center;gap:8px;font-size:25px;font-weight:600;color:var(--blue)}
.brand-mark{width:22px;height:22px;background:var(--blue);border-radius:3px}
.main-nav a{position:absolute;top:24px;font-size:14px;color:var(--ink);text-decoration:none;white-space:nowrap}
.main-nav .is-active{left:399px;top:21px;width:90px;height:27px;border:1px solid var(--blue);border-radius:14px;color:var(--blue);text-align:center;line-height:25px}
.btn-signup{position:absolute;left:807px;top:22px;width:82px;height:25px;border-radius:13px;background:var(--orange);color:var(--white);font-size:14px;text-align:center;line-height:25px}

/* hero */
.hero{position:absolute;left:0;top:67px;width:1026px;height:369px;background:var(--blue)}
.hero-kicker{position:absolute;left:0;width:666px;top:69px;text-align:center;font-size:12px;color:var(--white);font-weight:600}
.hero-title{position:absolute;left:136px;top:84px;font-size:35px;font-weight:600;color:var(--white);letter-spacing:-1px;white-space:nowrap}
.divider{position:absolute;height:0;border-top:1px dashed rgba(255,255,255,.7)}
.divider-gem{position:absolute;width:16px;height:16px;transform:rotate(45deg);background:var(--white)}
.hero-text{position:absolute;left:136px;top:165px;width:396px;font-size:13.8px;line-height:16.5px;color:var(--white);letter-spacing:-.2px}
.pay-badge{position:absolute;top:263px;height:24px;background:rgba(255,255,255,.35);border-radius:3px}
.btn-cta{position:absolute;left:335px;top:261px;width:185px;height:27px;border:1px solid var(--white);border-radius:14px;color:var(--white);font-size:13px;text-align:center;line-height:25px}
.monitor{position:absolute;left:557px;top:77px;width:333px;height:220px;background:var(--white);border-radius:6px}
.monitor-screen{position:absolute;left:10px;top:9px;width:315px;height:202px;background:linear-gradient(135deg,#8e9aa6,#c8bfb2 40%,#5d7fae 70%,#6d8398)}
.monitor-neck{position:absolute;left:712px;top:297px;width:28px;height:28px;background:var(--white)}
.monitor-base{position:absolute;left:660px;top:319px;width:126px;height:22px;background:var(--white);border-radius:63px 63px 0 0}
.monitor-arrows{position:absolute;left:713px;top:302px;font-size:12px;color:#aaa;letter-spacing:4px}

/* news */
.news-bar{position:absolute;left:0;top:436px;width:1026px;height:45px;background:var(--orange)}
.news-label{position:absolute;left:137px;top:13px;width:108px;height:20px;background:var(--ink);color:var(--white);font-size:11px;line-height:20px;padding-left:11px;border-radius:10px 0 0 10px;clip-path:polygon(0 0,92% 0,100% 50%,92% 100%,0 100%)}
.news-text{position:absolute;left:258px;top:15px;width:515px;font-size:11px;color:var(--white);letter-spacing:-.15px;white-space:nowrap;overflow:hidden}
.news-link{position:absolute;left:790px;top:19px;font-size:7.5px;color:var(--white);font-weight:600;white-space:nowrap}
.news-arrow{position:absolute;top:16px;width:12px;height:12px;transform:rotate(45deg);border:1px solid var(--white)}

/* features */
.features{position:absolute;left:0;top:481px;width:1026px;height:617px;background:var(--grey-light)}
.section-title{position:absolute;left:0;width:1026px;top:62px;text-align:center;font-size:28px;font-weight:800;letter-spacing:-1px}
.section-lead{position:absolute;left:0;width:1026px;top:104px;text-align:center;font-family:Arial,sans-serif;font-size:12px;color:var(--grey)}
.feature-card{position:absolute;top:176px;width:183px;height:147px;background:var(--white);box-shadow:0 2px 3px rgba(0,0,0,.25)}
.feature-icon{position:absolute;left:12px;top:25px}
.feature-title{position:absolute;left:62px;top:29px;font-size:12.5px;font-weight:700;color:var(--grey);white-space:nowrap}
.feature-text{position:absolute;left:62px;top:48px;width:108px;font-size:10px;line-height:13.6px;color:var(--grey);letter-spacing:-.3px}
.pill{position:absolute;height:13px;border-radius:7px;font-size:7px;color:var(--white);text-align:center;line-height:13px;font-weight:600;white-space:nowrap}
.pill.orange{background:var(--orange)}
.pill.grey{background:#999}
.pill.white{background:var(--white);color:var(--orange)}

.promo{position:absolute;top:364px;width:368px;height:203px;background:var(--blue)}
.promo-photo{position:absolute;left:22px;top:29px;width:129px;height:141px}
.promo-title{position:absolute;left:162px;top:28px;font-size:28px;font-weight:300;line-height:28px;color:var(--white);white-space:nowrap}
.promo-text{position:absolute;left:164px;top:89px;width:190px;font-size:10px;line-height:14px;color:var(--white);letter-spacing:-.3px}

/* footer */
.site-footer{position:absolute;left:0;top:1098px;width:1026px;height:102px;background:var(--white);border-top:1px solid #ccc}
.footer-links{position:absolute;left:136px;top:34px;font-size:10px;color:var(--muted);word-spacing:3px;white-space:nowrap}
.copyright{position:absolute;left:136px;top:50px;font-size:9.5px;color:var(--muted)}
.footer-rule{position:absolute;left:424px;top:24px;width:1px;height:55px;background:#bbb}
.app-brand{position:absolute;left:443px;top:28px;display:flex;align-items:center;gap:8px;font-size:34px;font-weight:400;color:#333;white-space:nowrap}
.app-mark{width:18px;height:28px;background:var(--blue);border-radius:3px}
.social{position:absolute;top:33px;width:24px;height:24px;transform:rotate(45deg);border:1px solid #bbb}
</style>
</head>
<body>

<header class="site-header">
  <div class="brand"><span class="brand-mark"></span>Paywisp</div>
  <nav class="main-nav">
    <a class="is-active" href="#">Home</a>
    <a href="#" style="left:494px">Payment</a>
    <a href="#" style="left:583px">Services</a>
    <a href="#" style="left:667px">About</a>
    <a href="#" style="left:737px">Contact</a>
  </nav>
  <a class="btn-signup">Signup</a>
</header>

<section class="hero">
  <div class="hero-kicker">YOUR</div>
  <h1 class="hero-title">Paywisp for Everywhere</h1>
  <div class="divider" style="left:139px;top:144px;width:388px"></div>
  <div class="divider-gem" style="left:325px;top:136px"></div>
  <p class="hero-text">Lorem ipsum dolor sit amet, consectetur adipisicing elit, sed do eiusmod tempor incididunt ut labore et lorem ipsum dolor sit amet, consectetur adipisicing elit, sed do eiusmod tempor incididunt ut labore et dolore magna aliqua.</p>
  <div class="pay-badge" style="left:137px;width:43px;border-radius:12px"></div>
  <div class="pay-badge" style="left:190px;width:47px"></div>
  <div class="pay-badge" style="left:246px;width:26px"></div>
  <div class="pay-badge" style="left:282px;width:36px"></div>
  <a class="btn-cta">Click on Call to Action</a>
  <div class="monitor">
    <div class="monitor-screen" role="img" aria-label="Photo of a hand swiping a payment card through a reader attached to a smartphone"></div>
  </div>
  <div class="monitor-neck"></div>
  <div class="monitor-base"></div>
  <div class="monitor-arrows">‹ ›</div>
</section>

<div class="news-bar">
  <div class="news-label">NEWS UPDATES</div>
  <div class="news-text">Lorem ipsum dolor sit amet, consectetur adipisicing elit, sed do eiusmod tempor incidi dunt ut labore ...</div>
  <div class="news-link">CLICK HERE</div>
  <div class="news-arrow" style="left:853px"></div>
  <div class="news-arrow" style="left:875px;background:var(--white)"></div>
</div>

<section class="features">
  <h2 class="section-title">Our Features</h2>
  <p class="section-lead">Lorem ipsum dolor sit amet, consectetur adipisicing elit, sed do eiusmod tempor incididunt ut labore et dolore magna aliqua.</p>
  <div class="divider" style="left:389px;top:146px;width:248px;border-color:#999"></div>
  <div class="divider-gem" style="left:505px;top:138px;background:var(--grey-light);border:1px solid #bbb"></div>

  <article class="feature-card" style="left:137px">
    <svg class="feature-icon" width="44" height="44" viewBox="0 0 44 44" fill="none" stroke="#3fa0cf" stroke-width="2.5"><path d="M6 22a16 16 0 1 0 5-11.5"/><path d="M13 15h3l3 12h12l3-9H17"/><circle cx="20" cy="31" r="1.8"/><circle cx="30" cy="31" r="1.8"/></svg>
    <h3 class="feature-title">Shopping Online</h3>
    <p class="feature-text">Lorem ipsum dolor sit amet, consectetur adipisicing elit, sed do eiusmod tempor incidi dunt ut labore</p>
    <a class="pill orange" style="left:61px;top:118px;width:53px">CLICK HERE</a>
  </article>
  <article class="feature-card" style="left:327px">
    <svg class="feature-icon" width="44" height="44" viewBox="0 0 44 44" fill="none" stroke="#3fa0cf" stroke-width="2.5"><path d="M6 22a16 16 0 1 0 5-11.5"/><circle cx="22" cy="22" r="10" fill="#3fa0cf"/></svg>
    <h3 class="feature-title">Selling Online</h3>
    <p class="feature-text">Lorem ipsum dolor sit amet, consectetur adipisicing elit, sed do eiusmod tempor incidi dunt ut labore</p>
    <a class="pill grey" style="left:61px;top:119px;width:53px">CLICK HERE</a>
  </article>
  <article class="feature-card" style="left:516px">
    <svg class="feature-icon" width="44" height="44" viewBox="0 0 44 44" fill="none" stroke="#3fa0cf" stroke-width="2.5"><path d="M6 22a16 16 0 1 0 5-11.5"/><path d="M14 14h9l9 9-8 8-10-9z" fill="#3fa0cf"/></svg>
    <h3 class="feature-title">Selling in Store</h3>
    <p class="feature-text">Lorem ipsum dolor sit amet, consectetur adipisicing elit, sed do eiusmod tempor incidi dunt ut labore</p>
    <a class="pill grey" style="left:61px;top:119px;width:53px">CLICK HERE</a>
  </article>
  <article class="feature-card" style="left:705px">
    <svg class="feature-icon" width="44" height="44" viewBox="0 0 44 44" fill="none" stroke="#3fa0cf" stroke-width="2.5"><path d="M6 22a16 16 0 1 0 5-11.5"/><rect x="14" y="15" width="16" height="14" rx="2" fill="#3fa0cf"/></svg>
    <h3 class="feature-title">Multiple Wallets</h3>
    <p class="feature-text">Lorem ipsum dolor sit amet, consectetur adipisicing elit, sed do eiusmod tempor incidi dunt ut labore</p>
    <a class="pill grey" style="left:61px;top:119px;width:53px">CLICK HERE</a>
  </article>

  <article class="promo" style="left:137px">
    <div class="promo-photo" role="img" aria-label="Illustration of a globe resting on banknotes" style="background:radial-gradient(circle at 55% 40%,#4f9bd6,#2a6aa8 45%,#c8c0a8 70%,#e9e2d0)"></div>
    <h3 class="promo-title">Global Money<br>Transfers</h3>
    <p class="promo-text">Lorem ipsum dolor sit amet, consectetur adipisicing elit, sed do eiusmod tempor incidi dunt ut labore lorem ipsum dolor sit amet, consectetur adipisicing elit, sed do eiusmod tempor incidi dunt ut labore lorem ipsum dolor sit amet,</p>
    <a class="pill orange" style="left:295px;top:172px;width:53px">CLICK HERE</a>
  </article>
  <article class="promo" style="left:521px">
    <div class="promo-photo" role="img" aria-label="Photo of a hand holding a smartphone" style="background:linear-gradient(120deg,#e8e8e8,#b9b2ad 50%,#6e6e70)"></div>
    <h3 class="promo-title">About Paywisp<br>Payment</h3>
    <p class="promo-text">Lorem ipsum dolor sit amet, consectetur adipisicing elit, sed do eiusmod tempor incidi dunt ut labore lorem ipsum dolor sit amet, consectetur adipisicing elit, sed do eiusmod tempor incidi dunt ut labore lorem ipsum dolor sit amet,</p>
    <a class="pill white" style="left:295px;top:172px;width:53px">CLICK HERE</a>
  </article>
</section>

<footer class="site-footer">
  <nav class="footer-links">Home &nbsp;- &nbsp;Payment &nbsp;- &nbsp;Services &nbsp;- &nbsp;About &nbsp;- &nbsp;Contact</nav>
  <p class="copyright">All Right Reserved © 2014</p>
  <div class="footer-rule"></div>
  <div class="app-brand"><span class="app-mark"></span>Paywisp App</div>
  <div class="social" style="left:779px"></div>
  <div class="social" style="left:817px"></div>
  <div class="social" style="left:855px"></div>
</footer>

</body>
</html>
```